Postcard Design

We'd like a postcard designed for our Crate O' Crunch subscription company. Our website is crateocrunch.example and we offer a monthly subscription box of snacks.
We'd like the final design to pop and offer engagement via social media etc. #crateocrunch is a hashtag we'd like used.
attached is our logo.
Updates

Please use the #crateocrunch as follows. "Take A Picture Of Your Crate O' Crunch To Be Featured On Our Site, And Have A Chance To Win A Free Month Of Snacks!"

Target Market(s)

College students, moms, kids.
People who love snacks.

Industry/Entity Type

It Company

Requirements
Must have
• Please use the #crateocrunch as follows.
"Take A Picture Of Your Crate O' Crunch And Use #CRATEOCRUNCH To Be Featured On Our Site, And Have A Chance To Win A Free Month Of Snacks!"

```html
<!DOCTYPE html>
<html lang="en">
<head>
<meta charset="utf-8">
<title>Crate O' Crunch Postcard</title>
<link rel="stylesheet" href="https://fonts.googleapis.com/css2?family=PT+Sans:wght@400;700&family=PT+Sans+Narrow:wght@400;700&display=swap">
<style>
  :root {
    --stage: #ecebe8;
    --cream: #fbf4e8;
    --cream-deep: #eadbc3;
    --orange: #c8622a;
    --orange-bright: #ee8a1c;
    --yellow: #f6c21a;
    --brown: #5a2a16;
    --brown-dark: #3f1c0e;
    --ink: #2a211d;
    --logo-tan: #e4a94e;
    --white: #ffffff;
    --rule: #b9b4ae;
    --social: #2e7fbf;
  }
  * { box-sizing: border-box; margin: 0; padding: 0; }
  html, body { width: 1200px; height: 500px; overflow: hidden; }
  body {
    background: var(--stage);
    font-family: "PT Sans", sans-serif;
    position: relative;
  }

  /* ---------- Front card ---------- */
  .card-front {
    position: absolute; left: 18px; top: 36px; width: 562px; height: 432px;
    background: linear-gradient(90deg, var(--yellow), var(--orange-bright));
    overflow: hidden;
  }
  .front-top {
    position: absolute; left: 0; top: 0; width: 100%; height: 170px;
    background: linear-gradient(90deg, var(--cream), var(--cream-deep));
  }
  .brand-block {
    position: absolute; left: 14px; top: 24px; width: 140px; text-align: center;
  }
  .brand-square {
    display: block; width: 62px; height: 62px; margin: 0 auto 18px;
    background: var(--logo-tan);
  }
  .brand-name {
    font-family: "PT Sans Narrow", sans-serif; font-weight: 700;
    font-size: 20px; color: var(--orange); white-space: nowrap;
  }
  .headline {
    position: absolute; left: 168px; top: 16px;
    font-family: "PT Sans Narrow", sans-serif; font-weight: 700;
    font-size: 25px; color: var(--orange); line-height: 1;
  }
  .front-url {
    position: absolute; left: 166px; top: 40px;
    font-family: "PT Sans Narrow", sans-serif; font-weight: 700;
    font-size: 23px; color: var(--brown-dark); white-space: nowrap;
  }
  .pitch {
    position: absolute; left: 164px; top: 68px; width: 374px; height: 108px;
    background: linear-gradient(90deg, var(--brown-dark), var(--orange));
    transform: rotate(-4deg);
    color: var(--white); font-family: "PT Sans Narrow", sans-serif;
    font-size: 17px; line-height: 1.22; padding: 18px 18px 0 22px;
  }
  .box-band {
    position: absolute; left: 0; top: 190px; width: 100%; height: 162px;
    background: var(--brown);
  }
  .box-option {
    position: absolute; top: 4px; width: 176px; text-align: center;
  }
  .box-option h2 {
    font-family: "PT Sans Narrow", sans-serif; font-weight: 700;
    font-size: 16px; color: var(--white); white-space: nowrap; margin-bottom: 10px;
  }
  .box-photo { display: block; margin: 0 auto; }
  .box-photo.classic { width: 121px; height: 121px; background: linear-gradient(135deg, #4e3f7a, #c9b13e); }
  .box-photo.healthy { width: 160px; height: 121px; background: linear-gradient(135deg, #c9a86c, #2f4d8a); }
  .box-photo.choc { width: 163px; height: 121px; background: linear-gradient(135deg, #b9422a, #2f5a8c); }
  .social-call {
    position: absolute; left: 0; top: 354px; width: 100%; text-align: center;
    font-family: "PT Sans Narrow", sans-serif; font-size: 17px; color: var(--brown-dark);
  }
  .social-list {
    position: absolute; left: 198px; top: 378px; display: flex; gap: 14px; list-style: none;
  }
  .social-list li { display: flex; flex-direction: column; align-items: center; width: 44px; }
  .social-dot { width: 36px; height: 36px; border-radius: 50%; background: var(--social); }
  .social-name {
    font-family: "PT Sans Narrow", sans-serif; font-size: 11px; color: var(--brown-dark); margin-top: 2px;
  }

  /* ---------- Back card ---------- */
  .card-back {
    position: absolute; left: 612px; top: 36px; width: 556px; height: 432px;
    background: var(--white);
  }
  .back-panel {
    position: absolute; left: 0; top: 0; width: 268px; height: 356px;
    background: linear-gradient(90deg, var(--cream), var(--cream-deep));
  }
  .signup {
    position: absolute; left: 62px; top: 14px; width: 204px;
    font-family: "PT Sans Narrow", sans-serif; font-weight: 700;
    font-size: 23px; line-height: 1.1; color: var(--ink); white-space: nowrap;
  }
  .back-url {
    position: absolute; left: 0; top: 66px; width: 268px; text-align: center;
    font-size: 20px; color: var(--ink); letter-spacing: 0.2px; white-space: nowrap;
  }
  .back-photo {
    position: absolute; left: 0; top: 94px; width: 268px; height: 142px;
    background: linear-gradient(120deg, #1d1d1d, #6c4fa8 45%, #e2b43a 70%, #c64a3a);
  }
  .refer-title {
    position: absolute; left: 18px; top: 242px;
    font-family: "PT Sans Narrow", sans-serif; font-weight: 700; font-size: 18px; color: var(--ink);
  }
  .refer-copy {
    position: absolute; left: 18px; top: 268px; width: 238px;
    font-family: "PT Sans Narrow", sans-serif; font-weight: 700; font-size: 14.5px;
    line-height: 1.38; color: var(--ink);
  }
  .contest {
    position: absolute; left: 18px; top: 368px; width: 520px;
    font-family: "PT Sans Narrow", sans-serif; font-weight: 700; font-size: 15px;
    line-height: 1.35; color: var(--ink);
  }
  .contest .hashtag { color: var(--orange); }
  .mail-brand {
    position: absolute; left: 306px; top: 18px; width: 160px; text-align: center;
  }
  .mail-brand .brand-square { width: 50px; height: 50px; margin-bottom: 12px; }
  .mail-brand .brand-name { font-size: 17px; font-family: "PT Sans", sans-serif; font-weight: 400; }
  .mail-url { font-size: 14px; color: var(--ink); }
  .stamp-box {
    position: absolute; left: 460px; top: 0; width: 83px; height: 94px;
    border: 1.5px solid var(--rule);
  }
  .address-lines { position: absolute; left: 306px; top: 196px; }
</style>
</head>
<body>

<section class="card-front">
  <div class="front-top"></div>
  <div class="brand-block">
    <span class="brand-square"></span>
    <span class="brand-name">Crate O' Crunch</span>
  </div>
  <h1 class="headline">Start Your Box Today!</h1>
  <p class="front-url">www.crateocrunch.example</p>
  <p class="pitch">When you sign up for Crate O' Crunch, every month you will receive a box of carefully selected snacks and munchies. A portion of every sale will go to a charitable cause.</p>

  <div class="box-band">
    <div class="box-option" style="left:14px">
      <h2>Classic Crate O' Crunch</h2>
      <div class="box-photo classic" role="img" aria-label="Photo of an open box of classic chips and candy snacks"></div>
    </div>
    <div class="box-option" style="left:188px">
      <h2>Healthy Crate O' Crunch</h2>
      <div class="box-photo healthy" role="img" aria-label="Photo of an open box of healthy snack bars and packs"></div>
    </div>
    <div class="box-option" style="left:366px">
      <h2>Chocolatey Crate O' Crunch</h2>
      <div class="box-photo choc" role="img" aria-label="Photo of an open box of chocolate candies and cookies"></div>
    </div>
  </div>

  <p class="social-call">Check us out on our social media sites!</p>
  <ul class="social-list">
    <li><span class="social-dot"></span><span class="social-name">Friendbook</span></li>
    <li><span class="social-dot"></span><span class="social-name">Chirper</span></li>
    <li><span class="social-dot"></span><span class="social-name">Snapgram</span></li>
  </ul>
</section>

<section class="card-back">
  <div class="back-panel">
    <h2 class="signup">Sign Up Now For A<br>Crate O' Crunch</h2>
    <p class="back-url">crateocrunch.example</p>
    <div class="back-photo" role="img" aria-label="Photo of stacked sandwich cookies with rainbow coloured fillings"></div>
    <h3 class="refer-title">Refer A Friend Program</h3>
    <p class="refer-copy">By referring ONLY two friends you can get a month of Crate O' Crunch delivered to your door for FREE.</p>
  </div>

  <p class="contest">Take A Picture Of Your Crate O' Crunch And Use <span class="hashtag">#CRATEOCRUNCH</span> To Be Featured On Our Site, And Have A Chance To Win A Free Month Of Snacks!</p>

  <div class="mail-brand">
    <span class="brand-square"></span>
    <p class="brand-name">Crate O' Crunch</p>
    <p class="mail-url">crateocrunch.example</p>
  </div>
  <div class="stamp-box"></div>

  <svg class="address-lines" width="240" height="110" viewBox="0 0 240 110">
    <g stroke="#b9b4ae" stroke-width="1.5">
      <line x1="0" y1="1" x2="237" y2="1"/>
      <line x1="0" y1="36" x2="237" y2="36"/>
      <line x1="0" y1="71" x2="237" y2="71"/>
      <line x1="0" y1="105" x2="237" y2="105"/>
    </g>
  </svg>
</section>

</body>
</html>
```